We Import and supply LED Lighting products (High Bays, Flood Lights, Bulbs, Down Lights, Strip Lighting, Night Lights.) and we are after a brochure design that communicates these product points below..

1. Environmentally Friendly.
2. Recyclable
3. Energy Saving
3. Cost Savings for the customer (big and small business)
4. Long Life Span.
5. Lower Maintenance Costs.
6. Importing
7. QUALITY PRODUCTS

The brochure needs to reflect that LED lighting is a safer 'lighting' solution for the environment and also to reflect big cost savings to big and small business ... I have highlighted some colours below but will leave this to the designer to decide on.

I have included some photos that resemble the type of other LED Lighting we sell.

Kind Regards

File 3 & File 5 can't be opened so please ignore.

Target Market(s)

Industrial / Warehousing... (Highbays & Flood Lights)
Domestic: ..... Bulbs & Strip Lighting

Industry/Entity Type

Small Business

Requirements
Must have
• Your professional experience in graphic design... show me that you can produce a professional look, not just a rush job with bad spelling.

Definitely depicts that we sell Quality LED Lighting with very competitive pricing.

Wholesale and Retail.

Our Logo.. this is the image I have uploaded, '"purple circle with grey wings"
Nice to have
• images and or symbols that depict recyclable, environmentally safe. energy saving and maybe a stack of coins that show money that can be saved (especially on the highbays)
Should not have
• copying the brochure I have uploaded and just adding colour!...

```html
<!DOCTYPE html>
<html lang="en">
<head>
<meta charset="utf-8">
<title>Lumora Imports – LED Lighting Brochure</title>
<link href="https://fonts.googleapis.com/css2?family=Delius&family=Arimo:wght@400;700&display=swap" rel="stylesheet">
<style>
  :root {
    --bg: #e4e4e1;
    --cream: #f5f7ea;
    --lime: #8dc63f;
    --green: #5cb82f;
    --green-dark: #3f8f22;
    --purple: #5a2a84;
    --pink: #d3348c;
    --white: #ffffff;
    --ink: #333333;
  }
  * { margin: 0; padding: 0; box-sizing: border-box; }
  html, body { width: 1200px; height: 1200px; overflow: hidden; background: var(--bg); }
  .spread {
    position: absolute; left: 60px; top: 215px;
    width: 1080px; height: 770px;
    display: flex;
    box-shadow: 0 6px 18px rgba(0,0,0,.18);
  }
  .panel { position: relative; width: 360px; height: 770px; overflow: hidden; }
  .panel + .panel { border-left: 1px solid rgba(0,0,0,.08); }

  /* Benefits panel */
  .benefits { background: var(--lime); color: var(--white); font-family: "Arimo", sans-serif; padding: 36px 30px 0 30px; }
  .benefits-title { font-family: "Delius", cursive; color: var(--purple); font-size: 22px; line-height: 1.2; margin-bottom: 12px; }
  .benefits p { font-size: 12.5px; line-height: 1.35; color: #fff; }
  .benefit-head { display: flex; align-items: center; gap: 10px; margin: 14px 0 6px; font-weight: 700; font-size: 15px; }
  .benefit-head svg { flex: none; }
  .bulb-art {
    position: absolute; left: 0; right: 0; bottom: 0; height: 200px;
    background: radial-gradient(ellipse at 55% 60%, #f4f9e6 0%, #d6ecad 45%, var(--lime) 80%);
  }

  /* Help panel */
  .help { background: var(--cream); font-family: "Arimo", sans-serif; }
  .help-title { position: absolute; left: 34px; top: 36px; font-family: "Delius", cursive; color: var(--purple); font-size: 20px; }
  .help-body { position: absolute; left: 34px; right: 30px; top: 76px; font-size: 13.5px; line-height: 1.6; color: var(--ink); text-align: justify; }
  .eco-badge {
    position: absolute; left: 70px; top: 230px; width: 220px; height: 140px; border-radius: 20px;
    background: radial-gradient(ellipse at 50% 40%, #b8e07a 0%, #6cbf35 50%, rgba(245,247,234,0) 80%);
  }
  .cert-row { position: absolute; left: 78px; top: 400px; display: flex; gap: 28px; }
  .cert { width: 38px; height: 38px; border-radius: 50%; background: var(--green); opacity: .85; }
  .cert.square { border-radius: 6px; }
  .wave { position: absolute; left: 0; top: 0; width: 360px; height: 770px; z-index: 1; }
  .contact {
    position: absolute; left: 0; right: 0; top: 640px; z-index: 2; text-align: center;
    color: var(--white); font-size: 13px; line-height: 1.4;
  }
  .contact strong { display: block; font-size: 15px; margin-bottom: 6px; }

  /* Cover panel */
  .cover { background: var(--cream); }
  .brand { position: absolute; left: 40px; top: 44px; display: flex; align-items: center; gap: 14px; }
  .brand-dot { width: 44px; height: 44px; border-radius: 50%; background: var(--purple); }
  .brand-name { font-family: "Delius", cursive; color: var(--purple); font-size: 22px; }
  .tagline { position: absolute; left: 0; right: 0; top: 130px; text-align: center; font-family: "Delius", cursive; font-size: 19px; line-height: 1.3; color: var(--purple); }
  .tagline .eco { color: var(--green); }
  .product-grid { position: absolute; left: 30px; top: 220px; }
  .band-label {
    position: absolute; left: 0; right: 0; top: 560px; height: 40px; line-height: 40px;
    text-align: center; font-family: "Delius", cursive; font-size: 17px; color: var(--white);
    background: var(--pink);
  }
  .cover-foot {
    position: absolute; left: 0; right: 0; top: 600px; bottom: 0; background: var(--green);
    padding-top: 40px; text-align: center; font-family: "Delius", cursive; font-size: 16px; line-height: 1.35; color: #1f3a10;
  }
</style>
</head>
<body>
<main class="spread">

  <section class="panel benefits">
    <h2 class="benefits-title">A few benefits of LED Lighting:</h2>
    <p>LED Lights are the most energy efficient lighting available today and most cost effective, they are made from non-toxic materials, generate virtually no heat and fully recyclable.</p>

    <div class="benefit-head">
      <svg width="22" height="22" viewBox="0 0 22 22"><circle cx="11" cy="11" r="9" fill="none" stroke="#fff" stroke-width="2"/><path d="M4 11h14M11 2c4 4 4 14 0 18M11 2c-4 4-4 14 0 18" fill="none" stroke="#fff" stroke-width="1.5"/></svg>
      Environmentally Friendly
    </div>
    <p>LED Lights are an eco-friendly form of lighting as they do not contain mercury or other harmful gasses or emit any harmful UV rays.</p>

    <div class="benefit-head">
      <svg width="22" height="22" viewBox="0 0 22 22"><circle cx="11" cy="12" r="8" fill="none" stroke="#fff" stroke-width="2"/><path d="M11 7v5l3 2" fill="none" stroke="#fff" stroke-width="2"/></svg>
      Long Life Span
    </div>
    <p>LED Lights have as uper long life span of 50,000 +hours considerably reducing your maintenance costs (no more blown lamp store place!)</p>

    <div class="benefit-head">
      <svg width="22" height="22" viewBox="0 0 22 22"><rect x="2" y="8" width="6" height="10" fill="#fff"/><path d="M8 10h8a2 2 0 010 4H8" fill="none" stroke="#fff" stroke-width="2"/></svg>
      Safety
    </div>
    <p>Most LED lights operate at low voltage so are cool to touch and much safer to handle during installation and maintenance.</p>

    <div class="benefit-head">
      <svg width="22" height="22" viewBox="0 0 22 22"><ellipse cx="11" cy="13" rx="5" ry="6" fill="#fff"/><path d="M3 9l4 2M19 9l-4 2M3 17l4-2M19 17l-4-2" stroke="#fff" stroke-width="2"/></svg>
      Insects:
    </div>
    <p>Insect attraction is greatly reduced due to minimal UV light and heat.</p>

    <div class="bulb-art" role="img" aria-label="Illustration of a glass light bulb with green seedling leaves growing inside from soil"></div>
  </section>

  <section class="panel help">
    <h2 class="help-title">We are here to help:</h2>
    <p class="help-body">You may have in mind other LED products not mentioned within this brochure; simply send an email with your enquiry with as much detail as possible and we would be happy to source and quote for you.</p>
    <div class="eco-badge" role="img" aria-label="Eco friendly badge with green leaves"></div>
    <div class="cert-row">
      <div class="cert"></div>
      <div class="cert"></div>
      <div class="cert square"></div>
      <div class="cert"></div>
    </div>
    <svg class="wave" viewBox="0 0 360 770" preserveAspectRatio="none">
      <path d="M0 584 C120 560 240 560 360 560 L360 600 L0 600 Z" fill="var(--pink)"/>
      <path d="M0 596 C120 574 240 574 360 600 L360 770 L0 770 Z" fill="var(--green)"/>
    </svg>
    <div class="contact">
      <strong>For all pricing and<br>quoting please contact:</strong>
      Mark Ellison<br>
      Mob: 0400 318 275<br>
      Email: sales@lumora-imports.example
    </div>
  </section>

  <section class="panel cover">
    <div class="brand">
      <span class="brand-dot"></span>
      <span class="brand-name">Lumora Imports</span>
    </div>
    <p class="tagline">Quality &amp; <span class="eco">Eco Friendly</span><br>LED Products</p>

    <svg class="product-grid" width="300" height="310" viewBox="0 0 300 310">
      <g stroke="#8dc63f" stroke-width="4" fill="#ffffff">
        <rect x="112" y="-8" width="96" height="96" transform="rotate(45 160 40)" />
        <rect x="42" y="82" width="96" height="96" transform="rotate(45 90 130)" />
        <rect x="182" y="82" width="96" height="96" transform="rotate(45 230 130)" />
        <rect x="112" y="172" width="96" height="96" transform="rotate(45 160 220)" />
      </g>
      <g>
        <rect x="122" y="2" width="76" height="76" transform="rotate(45 160 40)" fill="#d7d9d4" role="img" aria-label="Photo of an LED down light"/>
        <rect x="52" y="92" width="76" height="76" transform="rotate(45 90 130)" fill="#c9cbc6" role="img" aria-label="Photo of an LED bulb"/>
        <rect x="192" y="92" width="76" height="76" transform="rotate(45 230 130)" fill="#6f7fa6" role="img" aria-label="Photo of multicolour LED strip lighting"/>
        <rect x="122" y="182" width="76" height="76" transform="rotate(45 160 220)" fill="#cfcac0" role="img" aria-label="Photo of an LED flood light"/>
      </g>
    </svg>

    <div class="band-label">Importer &amp; Supplier</div>
    <div class="cover-foot">Bright Value Lighting<br>Wholesale/ Retail<br>Commercial / Domestic</div>
  </section>

</main>
</body>
</html>
```